Sports / Entertainment Media Co needs a biz card design

We are a media co / luxury lifestyle brand that targets professional athletes, entertainers and high net-worth fans. We are currently preparing for a relaunch and in need for new biz cards. I envision a black on black card with a pop of color on opposite side. Color Palette black, white, red etc. I want this card to exude sexiness and power. Very high stylized, hip and cool. I have attached the logo - I would like to see it all in black, but also open to other ideas. I will also upload a current card with all information needed on this new card. Furthermore I will add some samples of other cards I love. Thanks!!!

I provided suggestions, however I am open to all ideas!!   Be as creative as you can.  Think cutting-edge, sexy and powerful.  Take a look at the cards I uploaded to get a sense for what I like.  Thanks!!!

Entertainment

```html
<!DOCTYPE html>
<html lang="en">
<head>
<meta charset="utf-8">
<title>Strides – Business Card</title>
<link rel="stylesheet" href="https://fonts.googleapis.com/css2?family=Orbitron:wght@500;700;900&display=swap">
<style>
  :root {
    --ink: #0b0b0b;
    --paper: #f7f7f7;
    --paper-shade: #e6e6e6;
    --red: #f20d0d;
    --white: #ffffff;
    --stage: #d9d6d1;
  }
  * { margin: 0; padding: 0; box-sizing: border-box; }
  html, body {
    width: 1200px; height: 1019px; overflow: hidden;
    background: var(--stage);
    font-family: "Orbitron", "Arial", sans-serif;
  }
  .stage {
    position: relative; width: 1200px; height: 1019px;
    display: flex; justify-content: center; align-items: center; gap: 80px;
  }
  .card {
    position: relative; width: 360px; height: 630px; overflow: hidden;
    box-shadow: 0 14px 30px rgba(0,0,0,.25);
  }
  .card-back { background: var(--ink); }
  .card-front {
    background: linear-gradient(180deg, var(--white) 0%, var(--paper) 60%, var(--paper-shade) 100%);
  }
  .edge { position: absolute; top: 0; bottom: 0; width: 16px; background: var(--ink); }
  .edge-left { left: 0; }
  .edge-right { right: 0; }
  .brand {
    position: absolute; top: 92px; left: 0; right: 0;
    display: flex; justify-content: center; align-items: center; gap: 12px;
  }
  .brand-mark { width: 18px; height: 18px; background: var(--red); }
  .brand-name {
    font-weight: 900; font-size: 46px; color: var(--ink);
    text-transform: lowercase; letter-spacing: 1px;
  }
  .name-band {
    position: absolute; top: 238px; left: 0; right: 0; height: 92px;
    background: var(--red); color: var(--white);
    display: flex; flex-direction: column; justify-content: center; align-items: center;
    text-transform: uppercase;
  }
  .person-name { font-weight: 700; font-size: 22px; letter-spacing: 2px; }
  .person-title { font-weight: 500; font-size: 15px; letter-spacing: 2px; margin-top: 6px; }
  .contact-list {
    position: absolute; top: 362px; left: 34px; right: 24px;
    list-style: none; display: flex; flex-direction: column; gap: 12px;
  }
  .contact-item {
    display: flex; align-items: center; gap: 10px;
    font-size: 12px; font-weight: 500; color: var(--ink); letter-spacing: .5px;
  }
  .contact-icon {
    flex: 0 0 26px; width: 26px; height: 26px; border-radius: 4px;
    background: var(--ink); display: flex; align-items: center; justify-content: center;
  }
  .contact-icon svg { width: 16px; height: 16px; }
</style>
</head>
<body>
<main class="stage">
  <section class="card card-front">
    <div class="edge edge-left"></div>
    <div class="edge edge-right"></div>

    <div class="brand">
      <span class="brand-mark"></span>
      <span class="brand-name">strides</span>
    </div>

    <div class="name-band">
      <span class="person-name">Marcus Vale</span>
      <span class="person-title">General Manager</span>
    </div>

    <ul class="contact-list">
      <li class="contact-item">
        <span class="contact-icon"><svg viewBox="0 0 16 16"><path fill="#fff" d="M4 2l2 3-1.3 1.3a8 8 0 0 0 5 5L11 10l3 2-1 2.5C7.5 14.5 1.5 8.5 1.5 3z"/></svg></span>
        020 555 0143
      </li>
      <li class="contact-item">
        <span class="contact-icon"><svg viewBox="0 0 16 16"><rect x="4.5" y="1.5" width="7" height="13" rx="1.2" fill="none" stroke="#fff" stroke-width="1.4"/><circle cx="8" cy="12" r=".9" fill="#fff"/></svg></span>
        020 555 0144
      </li>
      <li class="contact-item">
        <span class="contact-icon"><svg viewBox="0 0 16 16"><rect x="4" y="2" width="8" height="4" fill="#fff"/><rect x="2" y="6.5" width="12" height="6" rx="1" fill="#fff"/><rect x="4.5" y="10" width="7" height="4" fill="#0b0b0b" stroke="#fff"/></svg></span>
        020 555 0145
      </li>
      <li class="contact-item">
        <span class="contact-icon"><svg viewBox="0 0 16 16"><rect x="2" y="4" width="12" height="8" fill="none" stroke="#fff" stroke-width="1.4"/><path d="M2 4l6 5 6-5" fill="none" stroke="#fff" stroke-width="1.4"/></svg></span>
        hello@stridesmedia.com
      </li>
      <li class="contact-item">
        <span class="contact-icon"><svg viewBox="0 0 16 16" fill="none" stroke="#fff" stroke-width="1.2"><circle cx="8" cy="8" r="6"/><ellipse cx="8" cy="8" rx="2.6" ry="6"/><path d="M2 8h12M3 5h10M3 11h10"/></svg></span>
        www.stridesmedia.com
      </li>
      <li class="contact-item">
        <span class="contact-icon"><svg viewBox="0 0 16 16"><path fill="#fff" d="M8 1.5a4.5 4.5 0 0 0-4.5 4.5c0 3.4 4.5 8.5 4.5 8.5s4.5-5.1 4.5-8.5A4.5 4.5 0 0 0 8 1.5z"/><circle cx="8" cy="6" r="1.7" fill="#0b0b0b"/></svg></span>
        41, 9th Floor, Harbor Line Road
      </li>
    </ul>
  </section>

  <section class="card card-back" aria-label="Card reverse, solid black"></section>
</main>
</body>
</html>
```